依頼詳細
ピラティス ヨガスタジオの看板デザインをお願いします。シンプルでわかりやすくスタイリッシュなイメージでお願いします。
記載項目
pilates&yoga studio VEL
希望イメージ
シンプル 複雑
単色 カラフル
暗い 明るい
日常 高級
遊び心 厳粛
未来的 伝統的
女性的 男性的
希望する色
無彩色系
納品ファイル
• 高解像度JPG (.jpg)
• PNG形式 (.png)
補足説明
写真の白い家の2階が店舗になります。
窓の下辺りに看板を出したいと思っています。壁に直接ペイントもしくは最後に添付しましたアイアン文字の様なイメージでできればと思っております。
高齢者にも分かりやすくピラティス&ヨガのカタカナをふって頂けると嬉しいです。
また、小さくてもいいので添付しましたロゴを入れて頂けると嬉しいです。
宜しくお願い致します。

シンプルで分かりやすく、ナチュラルな雰囲気がスタジオの雰囲気と合っていたので選びました。

皆様、素敵なデザインを提案して頂きありがとうございました。
また機会がありましたら、宜しくお願い致します。

```html
<!DOCTYPE html>
<html lang="ja">
<head>
<meta charset="utf-8">
<title>pilates&amp;yoga studio VEL — 看板</title>
<link rel="stylesheet" href="https://fonts.googleapis.com/css2?family=Noto+Sans+JP:wght@500;700;900&family=Montserrat:ital,wght@0,600;0,800;1,500&display=swap">
<style>
  :root {
    --backdrop: #eceeec;
    --sign-green: #8cc83c;
    --ink-white: #ffffff;
    --photo-a: #a7d463;
    --photo-b: #6f9e3a;
  }
  html, body {
    margin: 0;
    width: 900px;
    height: 1200px;
    overflow: hidden;
    background: var(--backdrop);
  }
  .canvas {
    position: relative;
    width: 900px;
    height: 1200px;
  }
  .signboard {
    position: absolute;
    left: 40px;
    top: 340px;
    width: 820px;
    height: 520px;
    background: var(--sign-green);
    box-shadow: 0 8px 24px rgba(0,0,0,0.15);
    overflow: hidden;
  }
  .pose-photo {
    position: absolute;
    left: 0;
    top: 0;
    width: 260px;
    height: 230px;
    display: block;
  }
  .studio-tagline {
    position: absolute;
    left: 290px;
    top: 40px;
    margin: 0;
    font-family: "Montserrat", sans-serif;
    font-style: italic;
    font-weight: 500;
    font-size: 34px;
    line-height: 1;
    letter-spacing: 1px;
    color: var(--ink-white);
    white-space: nowrap;
  }
  .brand-mark {
    position: absolute;
    right: 30px;
    top: 28px;
    width: 56px;
    height: 56px;
    background: var(--ink-white);
    border-radius: 8px;
  }
  .studio-name {
    position: absolute;
    left: 36px;
    top: 250px;
    margin: 0;
    font-family: "Noto Sans JP", sans-serif;
    font-weight: 900;
    color: var(--ink-white);
    line-height: 1.1;
  }
  .studio-name .kana {
    display: block;
    font-size: 72px;
    letter-spacing: 1px;
    white-space: nowrap;
  }
  .studio-name .brand {
    position: absolute;
    left: 448px;
    top: 18px;
    font-family: "Montserrat", sans-serif;
    font-weight: 800;
    font-size: 108px;
    line-height: 1;
    letter-spacing: 0;
    white-space: nowrap;
  }
  .trial-note {
    position: absolute;
    left: 36px;
    bottom: 28px;
    margin: 0;
    font-family: "Noto Sans JP", sans-serif;
    font-weight: 700;
    font-size: 40px;
    line-height: 1;
    letter-spacing: 3px;
    color: var(--ink-white);
    white-space: nowrap;
  }
  .brand-badge {
    position: absolute;
    right: 36px;
    bottom: 24px;
    width: 56px;
    height: 56px;
    border-radius: 50%;
    background: var(--ink-white);
  }
</style>
</head>
<body>
<main class="canvas">
  <section class="signboard">
    <svg class="pose-photo" viewBox="0 0 260 230" role="img" aria-label="Photo of two women doing a pilates stretch together">
      <defs>
        <linearGradient id="photoTone" x1="0" y1="0" x2="1" y2="1">
          <stop offset="0" stop-color="#a7d463"/>
          <stop offset="1" stop-color="#6f9e3a"/>
        </linearGradient>
      </defs>
      <rect width="260" height="230" fill="url(#photoTone)"/>
    </svg>
    <p class="studio-tagline">pilates &amp; yoga studio</p>
    <div class="brand-mark" aria-hidden="true"></div>
    <h1 class="studio-name">
      <span class="kana">ピラティス</span>
      <span class="kana">ヨガスタジオ</span>
      <span class="brand">&amp;VEL</span>
    </h1>
    <p class="trial-note">体験レッスンご予約受付中</p>
    <div class="brand-badge" aria-hidden="true"></div>
  </section>
</main>
</body>
</html>
```